BRINEWOOD PRODUCTIONS Video/Photo for Wedding/Events

We need a web design including the code which will be ready to launch. we are a Video and photography company in New Zealand and focus on medium to large Weddings and events.
The site will be our main point of contact with our customers with no more than 4-5 pages (Home, Pricing, Photo/Video Gallery, Contact) and we would like to be able to change the content of all pages as needed. The photos will be uploaded to our website but the videos we can only put the YouTube link.
I will add our company logo and some photos we have already taken to give you an idea of our product and services and can be used in the site as well.

Our pricing section will have photos, videos and photos + videos in 3 different pricing plans which we can upload and change as we need.

Here are some web pages to give you an idea of our industry and our competitors sites, however we would like the quality and design of our work to be better than all of our competitors sites which are listed below.

http://www.tallowpixel.example.nz/2012/02/9-great-new-zealand-photographers-websites/
http://rubquiphotography.example.uk/
http://www.doretavossphotography.example.nz/

Target Market(s)

our target audience is medium to up market customers who are looking at booking their wedding video/photography as well as events

Industry/Entity Type

Industry

Requirements
Must have
• The page must have a minimum of 4 pages, however we would like the designers to look outside the box and be creative with their designs.
Nice to have
• similar colors to our logo but don't limit your self and keep an open mind.

```html
<!DOCTYPE html>
<html lang="en">
<head>
<meta charset="utf-8">
<title>Brinewood Productions</title>
<link rel="stylesheet" href="https://fonts.googleapis.com/css2?family=Josefin+Sans:wght@300;400&family=Arimo:wght@400;700&display=swap">
<style>
  :root {
    --ink: #1e1d1b;
    --slate: #4b4944;
    --slate-deep: #3a3935;
    --panel: #f6f6f5;
    --teal: #4db6c4;
    --muted: #6f6d69;
    --rule: #8c8a86;
    --white: #ffffff;
  }
  * { margin: 0; padding: 0; box-sizing: border-box; }
  html, body { width: 1200px; height: 930px; overflow: hidden; background: var(--white); }
  .page { position: relative; width: 1200px; height: 930px; overflow: hidden; font-family: "Arimo", Arial, sans-serif; color: var(--ink); }

  .topbar { position: absolute; left: 0; top: 0; width: 1200px; height: 33px; background: var(--slate-deep); border-bottom: 2px solid var(--teal); }
  .social { position: absolute; left: 66px; top: 6px; display: flex; gap: 4px; }
  .social span { width: 19px; height: 19px; border-radius: 50%; border: 1.5px solid #d9d8d5; background: #5a5853; }

  .sidebar { position: absolute; left: 0; top: 35px; width: 234px; height: 895px; background: var(--panel); }
  .brand { position: absolute; left: 0; top: 13px; width: 234px; text-align: center; }
  .brand-dot { display: block; width: 80px; height: 80px; margin: 0 auto 12px; border-radius: 50%; background: var(--slate); }
  .brand-name { font-family: "Josefin Sans", sans-serif; font-weight: 400; color: var(--slate); font-size: 25px; letter-spacing: 2px; line-height: 1.1; }
  .brand-name small { display: block; font-size: 11px; letter-spacing: 4px; margin-top: 2px; }

  .nav { position: absolute; left: 0; top: 208px; width: 234px; list-style: none; text-align: center; font-family: "Josefin Sans", sans-serif; font-size: 17px; color: var(--ink); }
  .nav li { height: 36px; line-height: 36px; white-space: nowrap; }
  .nav .current { display: inline-block; position: relative; padding: 0 14px; }
  .nav .current svg { position: absolute; left: 0; top: 3px; }

  .nav-rule { position: absolute; left: 0; top: 346px; }

  .welcome { position: absolute; left: 24px; top: 385px; width: 205px; }
  .welcome h2 { font-family: "Josefin Sans", sans-serif; font-weight: 400; font-size: 26px; line-height: 26px; letter-spacing: 1px; margin-bottom: 10px; }
  .welcome p { font-size: 10.3px; line-height: 16.4px; color: #333; white-space: nowrap; }
  .welcome b { color: var(--ink); }
  .btn-dark { position: absolute; left: 23px; top: 601px; width: 95px; height: 22px; background: var(--slate-deep); color: var(--white); font-family: "Josefin Sans", sans-serif; font-size: 12px; letter-spacing: 1px; line-height: 24px; text-align: center; }

  .dotted { position: absolute; left: 0; width: 234px; height: 3px; border-top: 3px dotted var(--rule); }

  .tweets { position: absolute; left: 25px; top: 662px; width: 205px; }
  .tweets h3 { font-family: "Josefin Sans", sans-serif; font-weight: 300; font-size: 18px; line-height: 28px; letter-spacing: 1px; color: #333; display: flex; align-items: center; gap: 9px; white-space: nowrap; }
  .tweets h3 span { flex: none; width: 26px; height: 26px; border-radius: 50%; border: 2px solid #333; }
  .tweet-handle { font-size: 10.5px; font-weight: 700; margin-top: 12px; color: #333; }
  .tweet-text { font-size: 10px; line-height: 13.5px; color: var(--muted); margin-top: 9px; white-space: nowrap; }

  .copyright { position: absolute; left: 0; top: 844px; width: 224px; text-align: center; font-size: 11.5px; line-height: 19px; color: #555; }

  .hero { position: absolute; left: 234px; top: 35px; width: 966px; height: 608px;
    background: linear-gradient(180deg, #6c7a38 0%, #4a4a30 30%, #3e2f4e 55%, #5e4a55 70%, #d8d78a 88%, #eeeaa6 100%); }
  .hero-title { position: absolute; right: 103px; top: 303px; text-align: right; color: var(--white); font-family: "Josefin Sans", sans-serif; font-weight: 300; text-shadow: 2px 2px 2px rgba(0,0,0,.55); }
  .hero-title h1 { font-weight: 300; font-size: 60px; letter-spacing: 3px; line-height: 1; }
  .hero-title p { font-size: 31px; letter-spacing: 1px; margin-top: 6px; }
  .hero-arrow { position: absolute; top: 280px; }

  .gallery { position: absolute; left: 234px; top: 643px; width: 966px; height: 287px; background: var(--slate); }
  .gallery h2 { position: absolute; left: 49px; top: 20px; font-family: "Josefin Sans", sans-serif; font-weight: 300; font-size: 25px; color: var(--white); letter-spacing: 1.5px; }
  .btn-teal { position: absolute; left: 830px; top: 18px; width: 103px; height: 23px; background: var(--teal); color: var(--ink); font-family: "Josefin Sans", sans-serif; font-size: 12.5px; line-height: 25px; text-align: center; }
  .gallery-rule { position: absolute; left: 49px; top: 62px; width: 884px; border-top: 1px dotted #8e8b85; }
  .thumbs { position: absolute; left: 47px; top: 82px; display: flex; gap: 14px; }
  .thumb { width: 286px; height: 190px; border: 3px solid #3f3d39; }
  .thumb.rings { background: linear-gradient(135deg, #c9c6c2, #6d6a6e 50%, #e4e2e0); }
  .thumb.couple { border-color: #d8d8d6; background: linear-gradient(180deg, #f4f4f2, #b8a89a 50%, #efeeea); }
  .thumb.ceremony { background: linear-gradient(180deg, #2d3a24, #3f4a35 45%, #d9d6d0 75%, #b3b0a8); }
</style>
</head>
<body>
<div class="page">
  <header class="topbar">
    <div class="social" aria-label="Social links"><span></span><span></span><span></span><span></span><span></span></div>
  </header>

  <aside class="sidebar">
    <div class="brand">
      <span class="brand-dot"></span>
      <div class="brand-name">BRINEWOOD<small>PRODUCTIONS</small></div>
    </div>

    <ul class="nav">
      <li><span class="current">
        <svg width="80" height="30" viewBox="0 0 80 30" aria-hidden="true"><polygon points="8,1 72,1 79,15 72,29 8,29 1,15" fill="none" stroke="#8a8884" stroke-width="1"/></svg>
        HOME</span></li>
      <li>PRICING</li>
      <li>PHOTO/VIDEO GALLERY</li>
      <li>CONTACT</li>
    </ul>

    <svg class="nav-rule" width="234" height="20" viewBox="0 0 234 20" aria-hidden="true">
      <polyline points="0,1 117,17 234,1" fill="none" stroke="#c4c3c0" stroke-width="3"/>
    </svg>

    <section class="welcome">
      <h2>WELCOME!</h2>
      <p><b>Lorem ipsum dolor sit amet,<br>consectetuer adipiscing elit, sed diam<br>nonummy nibh euismod tincidunt ut<br>laoreet dolore magna aliquam erat<br>volutpat.</b> Ut wisi enim ad minim<br>veniam, quis nostrud exerci tation<br>ullamcorper suscipit lobortis nisl ut<br>aliquip ex ea commodo consequat.<br>Duis autem vel eum iriure dolor in<br>hendrerit in vulputate velit.</p>
    </section>
    <a class="btn-dark">READMORE</a>

    <div class="dotted" style="top:639px"></div>

    <section class="tweets">
      <h3>LATEST TWEETS <span></span></h3>
      <p class="tweet-handle">@tomas fenwick</p>
      <p class="tweet-text">Lorem ipsum dolor sit amet,<br>consectetuer adipiscing elit, sed<br>diam nonummy nibh e</p>
    </section>

    <div class="dotted" style="top:821px"></div>

    <p class="copyright">Copyright ©2013 Brinewood<br>Productions</p>
  </aside>

  <section class="hero" role="img" aria-label="Soft-focus wedding photograph of pale yellow petals in front of blurred garden lights">
    <svg class="hero-arrow" style="left:0" width="68" height="134" viewBox="0 0 68 134" aria-hidden="true">
      <path d="M0,0 A67,67 0 0 1 0,134 Z" fill="rgba(40,30,40,.45)"/>
      <polyline points="42,37 12,67 42,97" fill="none" stroke="#fff" stroke-width="5"/>
    </svg>
    <svg class="hero-arrow" style="right:0" width="68" height="134" viewBox="0 0 68 134" aria-hidden="true">
      <path d="M68,0 A67,67 0 0 0 68,134 Z" fill="rgba(40,30,40,.45)"/>
      <polyline points="26,37 56,67 26,97" fill="none" stroke="#fff" stroke-width="5"/>
    </svg>
    <div class="hero-title">
      <h1>BRINEWOOD</h1>
      <p>PRODUCTIONS</p>
    </div>
  </section>

  <section class="gallery">
    <h2>GALLERY</h2>
    <a class="btn-teal">VIEW GALLERY</a>
    <div class="gallery-rule"></div>
    <div class="thumbs">
      <div class="thumb rings" role="img" aria-label="Close-up of a ring being placed on the bride's hand"></div>
      <div class="thumb couple" role="img" aria-label="Portrait of a smiling bride and groom"></div>
      <div class="thumb ceremony" role="img" aria-label="White ceremony chairs with floral arrangements in a garden"></div>
    </div>
  </section>
</div>
</body>
</html>
```